Product Insert / Thank You

I'm looking for a small card to be designed that will be included with our product when it ships. It will be 2 sided with 1 side being a "thank you" with our logo and the other side containing the following text:We would love to hear your feedback! For every review we receive on our products, we donate 100% of the proceeds of your order to TIDEWELL -- a non profit organization dedicated to preserving our oceans!If you are not 100% satisfied with your purchase or have any problems, we will always resolve your issue. please contact us via Brindle if you need assistance.Insert needs to be well organized and information presented in a clear and visually appealing way.
Target Market(s)
Women, aged 24-45
Colors
Designer to choose colors to be used in the design.
Look and feel

```html
<!DOCTYPE html>
<html lang="en">
<head>
<meta charset="utf-8">
<title>Highwater Thank You Insert</title>
<link href="https://fonts.googleapis.com/css2?family=Arimo:wght@700&family=Didact+Gothic&family=Source+Sans+3:wght@400&display=swap" rel="stylesheet">
<style>
  :root {
    --page: #ffffff;
    --ink: #111111;
    --white: #ffffff;
    --sun: #fbe3cf;
    --peach: #e9a689;
    --coral: #c98478;
    --sea-light: #4fa3b0;
    --sea: #2a8fa0;
    --sea-deep: #1f5f82;
    --navy: #29507a;
  }
  * { margin: 0; padding: 0; box-sizing: border-box; }
  html, body {
    width: 848px;
    height: 1200px;
    overflow: hidden;
    background: var(--page);
  }
  .sheet {
    position: relative;
    width: 848px;
    height: 1200px;
  }
  .card {
    position: absolute;
    overflow: hidden;
  }
  .card--front { left: 165px; top: 106px; width: 537px; height: 379px; }
  .card--back  { left: 154px; top: 626px; width: 548px; height: 387px; }

  .card__photo {
    position: absolute;
    inset: 0;
    background:
      radial-gradient(ellipse 45% 30% at 42% 2%, var(--sun) 0%, rgba(251,227,207,0) 100%),
      linear-gradient(180deg, var(--peach) 0%, var(--coral) 14%, var(--sea-light) 36%, var(--sea) 62%, var(--sea-deep) 88%, var(--navy) 100%);
  }

  .brand-mark {
    position: absolute;
    display: flex;
    align-items: center;
    justify-content: center;
    border: 4px solid var(--ink);
    border-radius: 50%;
  }
  .brand-mark__name {
    font-family: "Didact Gothic", sans-serif;
    color: var(--ink);
    letter-spacing: 0.06em;
  }
  .brand-mark--large { left: 167px; top: 75px; width: 170px; height: 170px; }
  .brand-mark--large .brand-mark__name { font-size: 27px; }
  .brand-mark--small { left: 240px; top: 275px; width: 68px; height: 68px; border-width: 2px; }
  .brand-mark--small .brand-mark__name { font-size: 11px; }

  .thank-you {
    position: absolute;
    left: 0; right: 0; top: 270px;
    text-align: center;
    font-family: "Didact Gothic", sans-serif;
    font-size: 54px;
    color: var(--white);
    letter-spacing: 0.01em;
  }

  .feedback {
    position: absolute;
    left: 38px; right: 38px; top: 124px;
    text-align: center;
    font-family: "Arimo", sans-serif;
    font-weight: 700;
    font-size: 12.4px;
    line-height: 17.2px;
    color: var(--ink);
  }

  .side-label {
    position: absolute;
    left: 0; right: 0;
    text-align: center;
    font-family: "Source Sans 3", sans-serif;
    font-size: 56px;
    color: var(--ink);
  }
  .side-label--front { top: 490px; }
  .side-label--back  { top: 1052px; }
</style>
</head>
<body>
<main class="sheet">
  <section class="card card--front">
    <div class="card__photo" role="img" aria-label="Underwater view of sunlit ocean surface, warm light above turquoise water"></div>
    <div class="brand-mark brand-mark--large"><span class="brand-mark__name">HIGHWATER</span></div>
    <p class="thank-you">Thank you</p>
  </section>
  <p class="side-label side-label--front">Front</p>

  <section class="card card--back">
    <div class="card__photo" role="img" aria-label="Underwater view of sunlit ocean surface, warm light above turquoise water"></div>
    <p class="feedback">We would love to hear your feedback! For every review we receive on our products, we donate 100% of the proceeds of your order to TIDEWELL -- a non profit organization dedicated to preserving our oceans!If you are not 100% satisfied with your purchase or have any problems, we will always resolve your issue. please contact us via Brindle if you need assistance. Insert needs to be well organized and information presented in a clear and visually appealing way.</p>
    <div class="brand-mark brand-mark--small"><span class="brand-mark__name">HIGHWATER</span></div>
  </section>
  <p class="side-label side-label--back">Back</p>
</main>
</body>
</html>
```